Miles corbett biz card and stationary
Miles Corbett biz card
Bright & Fun-filled
Miles Corbett
Independent Agent
Pine Hollow, VT
miles.corbett@quillpost.com
please use the headshot we upload. see attachment for the logo.
please use the back of card content we upload.
headshot
card back content

```html
<!DOCTYPE html>
<html lang="en">
<head>
<meta charset="utf-8">
<title>Miles Corbett Stationery</title>
<link href="https://fonts.googleapis.com/css2?family=Open+Sans:wght@400;600;700&display=swap" rel="stylesheet">
<style>
  :root{
    --bg:#5f6063;
    --paper:#ffffff;
    --sky:#a9d3ef;
    --sky-light:#dcedf8;
    --ridge:#2c3440;
    --navy:#1d3f7a;
    --fax-blue:#2a5db0;
    --ink:#333a44;
    --muted:#8a9099;
    --field:#e6e8eb;
  }
  *{box-sizing:border-box;margin:0;padding:0}
  html,body{width:1200px;height:866px;overflow:hidden}
  body{background:var(--bg);font-family:"Open Sans",Arial,sans-serif;color:var(--ink);position:relative}

  .sheet{position:absolute;background:var(--paper);width:300px;height:400px;box-shadow:0 6px 18px rgba(0,0,0,.35)}
  .sheet--fax{left:40px;top:60px}
  .sheet--letter{left:370px;top:40px}

  .brand{display:flex;align-items:center;gap:5px}
  .brand__mark{width:10px;height:10px;border-radius:50%;background:var(--navy);flex:none}
  .brand__name{font-size:10px;font-weight:700;color:var(--navy);white-space:nowrap}

  .sheet__footer{position:absolute;left:0;right:0;bottom:0;height:38px;background:linear-gradient(180deg,var(--sky-light),var(--sky) 60%,var(--ridge))}
  .sheet__contact{position:absolute;left:14px;right:14px;bottom:44px;display:flex;justify-content:space-between;font-size:4.5px;color:var(--muted)}

  /* fax */
  .fax__head{display:flex;justify-content:space-between;align-items:center;padding:26px 16px 0}
  .fax__title{font-size:22px;font-weight:700;color:var(--fax-blue)}
  .fax__address{font-size:4.5px;color:var(--muted);padding:8px 16px 0;line-height:1.5}
  .fax__table{margin:12px 16px 0;border-top:6px solid var(--field)}
  .fax__row{display:grid;grid-template-columns:1fr 1fr;border-bottom:1px solid var(--field)}
  .fax__cell{font-size:5.5px;padding:4px;color:var(--ink)}
  .fax__cell b{font-weight:600}
  .fax__checks{display:flex;justify-content:space-between;margin:6px 16px 0;padding:4px;border:1px solid var(--field);font-size:5px}
  .fax__checks span::before{content:"";display:inline-block;width:5px;height:5px;border:1px solid var(--muted);margin-right:3px;vertical-align:-1px}
  .fax__notes{margin:8px 16px 0;height:110px;border-top:1px solid var(--field)}

  /* letter */
  .letter__head{justify-content:center;padding-top:22px}
  .letter__body{padding:22px 22px 0;font-size:5px;line-height:1.55;color:var(--ink)}
  .letter__body p{margin-bottom:6px}
  .letter__sign{font-size:10px;font-style:italic;color:var(--navy);margin-top:4px}

  /* envelope */
  .envelope{position:absolute;left:720px;top:190px;width:440px;height:200px;background:var(--paper);box-shadow:0 6px 18px rgba(0,0,0,.35);overflow:hidden}
  .envelope__band{position:absolute;left:0;right:0;bottom:0;height:56px;background:linear-gradient(180deg,var(--sky-light),var(--sky))}
  .envelope__flap{position:absolute;left:0;top:0;width:440px;height:70px}
  .envelope__brand{position:absolute;left:0;right:0;top:24px;justify-content:center}
  .envelope__window{position:absolute;left:250px;top:92px;width:140px;height:40px;border:1px solid #9aa3ad;border-radius:6px;background:rgba(255,255,255,.7)}
  .envelope__return{position:absolute;left:18px;top:84px;font-size:5px;color:var(--muted);line-height:1.5}

  /* cards */
  .card{position:absolute;width:340px;height:195px;box-shadow:0 6px 18px rgba(0,0,0,.35);overflow:hidden}
  .card--back{left:250px;top:560px;background:linear-gradient(135deg,var(--sky-light),var(--sky))}
  .card--front{left:620px;top:610px;background:var(--paper)}
  .card__pitch{position:absolute;left:20px;top:22px;width:300px;font-size:11px;font-weight:700;color:var(--navy);line-height:1.3}
  .card__badge{position:absolute;left:20px;top:100px;width:44px;height:44px;background:var(--navy)}
  .card__list{position:absolute;left:76px;top:100px;font-size:7px;color:var(--ink);line-height:1.6}
  .card__web{position:absolute;left:20px;bottom:14px;font-size:7px;color:var(--navy);font-weight:600}

  .card__photo{position:absolute;left:0;top:0;width:120px;height:195px;background:linear-gradient(180deg,#cfd8e0,#7f8fa3)}
  .card__brand{position:absolute;left:120px;right:0;top:40px;justify-content:center;gap:7px}
  .card__brand .brand__mark{width:16px;height:16px}
  .card__brand .brand__name{font-size:16px}
  .card__name{position:absolute;left:140px;top:112px;font-size:13px;font-weight:700;color:var(--navy)}
  .card__role{position:absolute;left:140px;top:132px;font-size:7.5px;color:var(--muted)}
  .card__contact{position:absolute;right:12px;top:112px;font-size:6px;color:var(--ink);line-height:1.6;text-align:right;width:100px}
  .card__base{position:absolute;left:120px;right:0;bottom:0;height:26px;background:linear-gradient(180deg,var(--sky),var(--ridge))}
</style>
</head>
<body>

<section class="sheet sheet--fax">
  <header class="fax__head">
    <div class="brand"><span class="brand__mark"></span><span class="brand__name">Corbett Agency</span></div>
    <h1 class="fax__title">FAX</h1>
  </header>
  <div class="fax__address">Pine Hollow, VT<br>336-555-0148</div>
  <div class="fax__table">
    <div class="fax__row"><div class="fax__cell"><b>To</b></div><div class="fax__cell"><b>From</b></div></div>
    <div class="fax__row"><div class="fax__cell"><b>Company</b></div><div class="fax__cell"><b>Date</b></div></div>
    <div class="fax__row"><div class="fax__cell"><b>Phone</b></div><div class="fax__cell"><b>Pages</b></div></div>
    <div class="fax__row"><div class="fax__cell"><b>Fax</b></div><div class="fax__cell"><b>CC</b></div></div>
    <div class="fax__row"><div class="fax__cell"><b>Re</b></div><div class="fax__cell"></div></div>
  </div>
  <div class="fax__checks">
    <span>Urgent</span><span>For Review</span><span>Please Comment</span><span>Please Reply</span>
  </div>
  <div class="fax__notes"></div>
  <div class="sheet__contact"><span>336-555-0148</span><span>miles.corbett@quillpost.com</span><span>Pine Hollow, VT</span></div>
  <div class="sheet__footer" role="img" aria-label="Blue mountain ridge band"></div>
</section>

<section class="sheet sheet--letter">
  <header class="letter__head brand"><span class="brand__mark"></span><span class="brand__name">Corbett Agency</span></header>
  <div class="letter__body">
    <p>21 June 2024<br>Dear Mr. Jones,</p>
    <p>Thank you for choosing our agency. We look forward to helping you review your coverage and plan for the years ahead with care.</p>
    <p>Our team works with many trusted carriers to find options for home, auto, life and business needs at a fair price.</p>
    <p>Please call or write anytime with questions. We are glad to meet in person and go over every detail together.</p>
    <p>Yours Sincerely,</p>
    <div class="letter__sign">Miles Corbett</div>
  </div>
  <div class="sheet__contact"><span>336-555-0148</span><span>miles.corbett@quillpost.com</span><span>Pine Hollow, VT</span></div>
  <div class="sheet__footer" role="img" aria-label="Blue mountain ridge band"></div>
</section>

<section class="envelope">
  <svg class="envelope__flap" viewBox="0 0 440 70" aria-hidden="true">
    <polygon points="0,0 440,0 220,70" fill="#eef3f7" stroke="#c9d2db" stroke-width="1"/>
  </svg>
  <div class="envelope__brand brand"><span class="brand__mark"></span><span class="brand__name">Corbett Agency</span></div>
  <div class="envelope__return">Corbett Agency<br>Pine Hollow, VT<br>336-555-0148</div>
  <div class="envelope__window"></div>
  <div class="envelope__band"></div>
</section>

<section class="card card--back">
  <p class="card__pitch">I represent many top companies that offer the products and services you may need to be better protected and prepared for your future.</p>
  <div class="card__badge"></div>
  <div class="card__list">Life, Home &amp; Auto<br>Health &amp; Medicare<br>Business Coverage<br>Retirement Planning</div>
  <div class="card__web">www.northridgecover.com</div>
</section>

<section class="card card--front">
  <div class="card__photo" role="img" aria-label="Headshot of Miles Corbett"></div>
  <div class="card__brand brand"><span class="brand__mark"></span><span class="brand__name">Corbett Agency</span></div>
  <div class="card__name">Miles Corbett</div>
  <div class="card__role">Independent Agent</div>
  <div class="card__contact">Pine Hollow, VT<br>336-555-0148<br>miles.corbett@quillpost.com</div>
  <div class="card__base" role="img" aria-label="Blue mountain ridge band"></div>
</section>

</body>
</html>
```